QDV Construction and Remodeling

Prefer a matte black card with some colors that pop, but subtle. Contact info. Show General Contractor professional way. Can you please remove renovations repairs maintenance off of my logo.

Target Market(s)

Property and business investors. Homeowners

Industry/Entity Type

Construction

Contact Information for Business Card

Name: Dorian Falkner, Title: CEO, Phone: 555-216-0394, Email: Dorian@QDVbuildTrx.com, website: www QDVbuildTrx.com

Font styles to use
Other font styles liked:
• Designer choose

Colors

Designer to choose colors to be used in the design.

Requirements
Must have
• Uniqueness. Double sided since it wont let me choose that. Professional look, be eye catching and catchy. QR code to my website
Nice to have
• Matte black background, subtle bright colors that pop, but I am open to anything. I also like black and gold with some red. Possible Harborton Ironclad logo colored stars somewhere around the logo or on the back. Just to rep my city
Should not have
• pink. Something you would see somewhere else. gif pictures or generated pictures.

```html
<!DOCTYPE html>
<html lang="en">
<head>
<meta charset="UTF-8">
<title>QDV Construction and Remodeling – Business Card</title>
<link href="https://fonts.googleapis.com/css2?family=Arimo:wght@400;700&display=swap" rel="stylesheet">
<style>
  :root {
    --page-bg: #e9e9ea;
    --card-white: #ffffff;
    --card-black: #1b1c1e;
    --accent-red: #e4131b;
    --ink: #141414;
    --rule: #3a3a3a;
    --logo-grey: #8d8e92;
    --qr-tile: #2a2b2e;
  }
  * { box-sizing: border-box; margin: 0; padding: 0; }
  html, body {
    width: 1200px; height: 1200px; overflow: hidden;
    background: var(--page-bg);
    font-family: "Arimo", Arial, sans-serif;
  }
  .sheet {
    position: relative; width: 1200px; height: 1200px;
    display: flex; justify-content: center; align-items: center; gap: 60px;
  }
  .card {
    width: 400px; height: 700px; border-radius: 30px;
    position: relative; overflow: hidden;
    box-shadow: 0 6px 18px rgba(0,0,0,0.18);
  }
  .card--front { background: var(--card-white); color: var(--ink); }
  .card--back {
    background: var(--card-black);
    display: flex; flex-direction: column; align-items: center; justify-content: center; gap: 60px;
  }

  .wordmark { display: flex; align-items: center; gap: 14px; }
  .wordmark__square { width: 22px; height: 22px; background: var(--accent-red); flex: none; }
  .wordmark__text { font-weight: 700; line-height: 1.05; text-transform: uppercase; }
  .wordmark__initials { display: block; font-size: 64px; letter-spacing: 1px; }
  .wordmark__name { display: block; font-size: 14px; letter-spacing: 2px; margin-top: 4px; }

  .card--front .wordmark { position: absolute; top: 110px; left: 0; right: 0; justify-content: center; }
  .card--front .wordmark__text { color: var(--ink); }
  .card--back .wordmark__text { color: var(--logo-grey); }

  .identity { position: absolute; top: 300px; left: 0; right: 0; text-align: center; }
  .identity__name { color: var(--accent-red); font-size: 31px; font-weight: 700; letter-spacing: 0.5px; text-transform: uppercase; }
  .identity__title { font-size: 25px; margin-top: 4px; }

  .icon-rule { position: absolute; top: 392px; left: 40px; right: 40px; display: flex; align-items: center; gap: 10px; }
  .icon-rule__line { flex: 1; height: 1px; background: var(--rule); }
  .icon { width: 36px; height: 36px; border-radius: 8px; background: var(--accent-red); display: flex; align-items: center; justify-content: center; }
  .icon svg { width: 24px; height: 24px; }

  .contact { position: absolute; top: 448px; left: 0; right: 0; text-align: center; font-size: 24px; line-height: 1.36; }

  .divider { position: absolute; top: 572px; left: 40px; right: 40px; height: 1px; background: var(--rule); }

  .address { position: absolute; top: 590px; left: 0; right: 0; text-align: center; font-size: 24px; line-height: 1.34; }

  .qr-slot {
    width: 110px; height: 110px; border-radius: 8px;
    background: var(--qr-tile);
    border: 2px solid var(--accent-red);
  }
</style>
</head>
<body>
<main class="sheet">

  <section class="card card--front">
    <div class="wordmark">
      <span class="wordmark__square"></span>
      <span class="wordmark__text">
        <span class="wordmark__initials">QDV</span>
        <span class="wordmark__name">Construction &amp; Remodeling</span>
      </span>
    </div>

    <div class="identity">
      <p class="identity__name">Dorian Falkner</p>
      <p class="identity__title">CEO</p>
    </div>

    <div class="icon-rule">
      <span class="icon-rule__line"></span>
      <span class="icon" aria-label="Phone">
        <svg viewBox="0 0 24 24" fill="none" stroke="#fff" stroke-width="2" stroke-linecap="round" stroke-linejoin="round">
          <path d="M6 3h3l2 5-2.5 1.5a11 11 0 0 0 6 6L16 13l5 2v3a2 2 0 0 1-2 2A16 16 0 0 1 4 5a2 2 0 0 1 2-2z"/>
        </svg>
      </span>
      <span class="icon" aria-label="Email">
        <svg viewBox="0 0 24 24" fill="none" stroke="#fff" stroke-width="2" stroke-linejoin="round">
          <rect x="3" y="5" width="18" height="14" rx="1"/>
          <path d="M3 6l9 7 9-7"/>
        </svg>
      </span>
      <span class="icon" aria-label="Website">
        <svg viewBox="0 0 24 24" fill="none" stroke="#fff" stroke-width="2">
          <circle cx="12" cy="12" r="9"/>
          <ellipse cx="12" cy="12" rx="4" ry="9"/>
          <path d="M3 12h18"/>
        </svg>
      </span>
      <span class="icon-rule__line"></span>
    </div>

    <div class="contact">
      <p class="contact__phone">555.216.0394</p>
      <p class="contact__email">Dorian@QDVbuildTrx.com</p>
      <p class="contact__web">www.QDVbuildTrx.com</p>
    </div>

    <div class="divider"></div>

    <div class="address">
      <p>Your address, city</p>
      <p>state, ZIP 0000</p>
    </div>
  </section>

  <section class="card card--back">
    <div class="wordmark">
      <span class="wordmark__square"></span>
      <span class="wordmark__text">
        <span class="wordmark__initials">QDV</span>
        <span class="wordmark__name">Construction &amp; Remodeling</span>
      </span>
    </div>
    <div class="qr-slot" role="img" aria-label="QR code linking to www.QDVbuildTrx.com"></div>
  </section>

</main>
</body>
</html>
```